Carpentry company Needs a business card design

We need a design for a Carpentry / building company, business card. Please think of designs out of the ordinary and try to make it eye catching. Our existing logo will need to be incorporated in the design. However feel free to change the colours of the logo to suit your design. I would like to see some designs with green /black and orange incorporated into it.These are not the only colours accepted and all designs that appeal will be accepted.

Please contact me should you have any questions
Thanks Martin

Target Market(s)

General Public seeking carpentry work

Industry/Entity Type

Business

Contact Information for Business Card

- Current company logo ( colours can be changed)
-Phone number ,
- info@brelvanbuild.com.au
- brelvanbuild.com.au
-the facebook symbol

Font styles to use
Other font styles liked:
• You choose

Requirements
Must have
• Services we provide
• - Renovations
• -Deckings & Pergolas
• -Kitchens
• - Bathrooms
• - Intricate details
Nice to have
• an awesome design
Should not have
• Tools on the business card

```html
<!DOCTYPE html>
<html lang="en">
<head>
<meta charset="utf-8">
<title>Brelvan Build – Business Card</title>
<link href="https://fonts.googleapis.com/css2?family=Roboto:wght@400;500;700&display=swap" rel="stylesheet">
<style>
  :root {
    --bg: #d9d6d2;
    --card: #262626;
    --card-back: #1b1b1b;
    --emboss: #0f0f0f;
    --green: #7ed321;
    --grey: #a7a7a7;
    --white: #ffffff;
    --muted: #d8d8d8;
  }
  * { margin: 0; padding: 0; box-sizing: border-box; }
  html, body { width: 1200px; height: 716px; overflow: hidden; }
  body {
    background: var(--bg);
    font-family: "Roboto", sans-serif;
    position: relative;
  }
  .card {
    position: absolute;
    top: 203px;
    width: 540px;
    height: 310px;
    border-radius: 4px;
    overflow: hidden;
    box-shadow: 0 6px 18px rgba(0,0,0,.25);
  }
  .card--back { left: 40px; background: var(--card-back); }
  .card--front { left: 620px; background: var(--card); }

  .back-brand {
    position: absolute; inset: 0;
    display: flex; align-items: center; justify-content: center; gap: 14px;
    font-weight: 700; font-size: 40px; letter-spacing: 2px;
    color: var(--emboss);
  }
  .back-brand .mark { width: 22px; height: 22px; background: var(--emboss); }

  .brand {
    position: absolute; left: 30px; top: 36px;
    display: flex; align-items: center; gap: 12px;
    font-weight: 700; font-size: 32px; letter-spacing: 1px;
    color: var(--white);
  }
  .brand .mark { width: 18px; height: 18px; background: var(--green); }
  .brand-bar {
    position: absolute; left: 30px; top: 88px;
    width: 90px; height: 5px; background: var(--green);
  }
  .divider {
    position: absolute; left: 30px; top: 112px;
    width: 330px; height: 1px; background: var(--green);
  }
  .services {
    position: absolute; left: 30px; top: 124px;
    color: var(--white); font-size: 13px; line-height: 17px;
  }
  .services h3 { font-size: 13px; font-weight: 700; }
  .services li { list-style: none; }
  .services li::before { content: "» "; }

  .person {
    position: absolute; right: 30px; top: 146px; text-align: right;
    color: var(--white);
  }
  .person .name { font-size: 19px; font-weight: 700; }
  .person .role { font-size: 12px; color: var(--muted); margin-top: 2px; }

  .contacts {
    position: absolute; right: 22px; top: 196px;
    color: var(--white); font-size: 12.5px;
  }
  .contacts li {
    list-style: none; display: flex; align-items: center; justify-content: flex-end;
    gap: 8px; height: 16px;
  }
  .icon { width: 11px; height: 11px; background: var(--green); display: block; }

  .bands { position: absolute; left: 0; bottom: 0; }
</style>
</head>
<body>
  <section class="card card--back" aria-label="Card back">
    <div class="back-brand"><span class="mark"></span>BRELVAN BUILD</div>
  </section>

  <section class="card card--front" aria-label="Card front">
    <div class="brand"><span class="mark"></span>BRELVAN BUILD</div>
    <div class="brand-bar"></div>
    <div class="divider"></div>

    <div class="services">
      <h3>Services we provide :</h3>
      <ul>
        <li>Renovations</li>
        <li>Intricate details</li>
        <li>Deckings &amp; Pergolas</li>
        <li>Kitchens &nbsp;» Bathrooms</li>
      </ul>
    </div>

    <div class="person">
      <div class="name">Your Good Name</div>
      <div class="role">Managing Director</div>
    </div>

    <ul class="contacts">
      <li>0412 555 018
        <svg class="icon" viewBox="0 0 11 11"><rect width="11" height="11" fill="#7ed321"/><path d="M3 2.5h1.6l.6 1.6-.9.7a4 4 0 0 0 1.9 1.9l.7-.9 1.6.6V8A.6.6 0 0 1 7.9 8.6 5.6 5.6 0 0 1 2.4 3.1.6.6 0 0 1 3 2.5z" fill="#262626"/></svg>
      </li>
      <li>info@brelvanbuild.com.au
        <svg class="icon" viewBox="0 0 11 11"><rect width="11" height="11" fill="#7ed321"/><rect x="2" y="3" width="7" height="5" fill="none" stroke="#262626"/><path d="M2 3l3.5 3L9 3" fill="none" stroke="#262626"/></svg>
      </li>
      <li>www.brelvanbuild.com.au
        <svg class="icon" viewBox="0 0 11 11"><rect width="11" height="11" fill="#7ed321"/><circle cx="5.5" cy="5.5" r="3.3" fill="none" stroke="#262626"/><path d="M2.2 5.5h6.6M5.5 2.2v6.6" stroke="#262626" stroke-width=".8"/></svg>
      </li>
      <li>/Brelvan-Build <span class="icon"></span></li>
    </ul>

    <svg class="bands" width="540" height="44" viewBox="0 0 540 44">
      <polygon points="0,10 248,10 224,44 0,44" fill="#7ed321"/>
      <polygon points="0,20 240,20 226,44 0,44" fill="#262626" opacity=".0"/>
      <polygon points="262,4 540,4 540,44 234,44" fill="#a7a7a7"/>
    </svg>
  </section>
</body>
</html>
```